Website Design, Ecommerce, Device Buyback, Four concepct pages

Full website design, concept and select pages.
* Home page
* Device catalog
* Order Summary

Require all design assets:
+ static images
+ color pallettes
+ fonts
Would prefer 'atomic' design elements.

Current concept site: http://vrlm.q7webnest.com/
Updates

Need extra days to review

Target Market(s)

us retail

Industry/Entity Type

Ecommerce

Number of Pages Required

3 page

Font styles to use
Serif
Sans Serif

Requirements
Must have
• * Home page
* Device catalog
* Order Summary
* Informational page

+ static images
+ color pallettes
+ fonts
Nice to have
• Would prefer 'atomic' design elements.
Additional pages nice to have:
* Form pages, eg contact form, login form
* Reviews page
* Back office pages: user management, catalog management, order management, etc.

```html
<!DOCTYPE html>
<html lang="en">
<head>
<meta charset="utf-8">
<title>FixTrade – Home</title>
<link href="https://fonts.googleapis.com/css2?family=Roboto+Condensed:ital,wght@0,400;0,700;1,400&family=Roboto:wght@400;500&display=swap" rel="stylesheet">
<style>
  :root {
    --backdrop: #eceef1;
    --page: #ffffff;
    --band: #f2f2f2;
    --blue: #1a7fc9;
    --teal: #1c5e7e;
    --pink: #f0359e;
    --pink-soft: #f7a3cf;
    --green: #1fe04e;
    --grey-text: #8a8a8a;
    --card-grey: #ececec;
    --star: #f5d21a;
    --phones-tone: #6f8599;
    --tablets-tone: #8797a8;
  }
  * { box-sizing: border-box; margin: 0; padding: 0; }
  html, body { width: 1200px; height: 784px; overflow: hidden; }
  body { background: var(--backdrop); font-family: "Roboto Condensed", "Roboto", sans-serif; position: relative; }
  h1, h2, h3, h4 { font-weight: 400; }

  .page {
    position: absolute; left: 311px; top: 0;
    width: 798px; height: 1082px;
    transform: scale(0.7246); transform-origin: top left;
    background: var(--page);
    box-shadow: 0 20px 40px rgba(0,0,0,.18);
    overflow: hidden;
  }
  .abs { position: absolute; }

  /* header */
  .site-header { left: 0; top: 0; width: 798px; height: 90px; background: var(--band); }
  .brand { left: 100px; top: 26px; display: flex; align-items: center; gap: 8px; }
  .brand-mark { width: 26px; height: 26px; background: var(--blue); border-radius: 4px; }
  .brand-name { font-size: 22px; font-weight: 700; color: var(--blue); }
  .nav { top: 38px; left: 527px; display: flex; gap: 27px; font-size: 9px; color: var(--blue); letter-spacing: .2px; }
  .account { left: 682px; top: 35px; }

  /* categories */
  .category { top: 144px; width: 288px; height: 315px; text-align: center; color: #fff; }
  .category-phones { left: 100px; background: linear-gradient(180deg, #7a8ea1 0%, var(--phones-tone) 55%, #4d6478 100%); }
  .category-tablets { left: 410px; background: linear-gradient(160deg, #8a9aa9 0%, var(--tablets-tone) 60%, #91a0af 100%); }
  .category-title { position: absolute; top: 114px; width: 100%; font-size: 19px; }
  .category-sub { position: absolute; top: 142px; width: 100%; font-size: 10.5px; }
  .browse-btn { position: absolute; top: 166px; left: 80px; width: 128px; height: 33px; background: var(--green); border-radius: 2px; font-size: 10px; line-height: 33px; color: #fff; }

  /* steps */
  .step { top: 512px; width: 177px; height: 96px; background: var(--card-grey); box-shadow: 0 3px 8px rgba(0,0,0,.15); padding: 9px 11px 0; text-align: center; }
  .step-title { font-size: 19px; color: var(--teal); margin-bottom: 11px; }
  .step-body { font-family: "Roboto", sans-serif; font-size: 6px; line-height: 9.5px; color: var(--grey-text); text-align: left; }
  .step-body a { color: var(--blue); text-decoration: none; }

  /* reviews */
  .reviews-title { top: 678px; left: 0; width: 798px; text-align: center; font-size: 18px; color: var(--pink); }
  .review { top: 726px; width: 173px; height: 150px; background: #fff; box-shadow: 0 2px 8px rgba(0,0,0,.14); padding: 15px 13px; }
  .reviewer { display: flex; align-items: center; gap: 5px; font-size: 10.5px; color: var(--blue); }
  .avatar { width: 29px; height: 29px; border-radius: 50%; background: linear-gradient(135deg, #b46a4a, #5d4a45); }
  .review-source { font-size: 12.5px; color: var(--blue); margin: 9px 0 6px; }
  .review-text { font-family: "Roboto", sans-serif; font-style: italic; font-size: 6.5px; line-height: 14px; color: var(--grey-text); padding-right: 14px; }
  .stars { margin-top: 4px; display: flex; gap: 1px; }
  .dots { top: 900px; left: 373px; display: flex; align-items: center; gap: 6px; }
  .dot { width: 11px; height: 11px; border-radius: 50%; background: var(--pink-soft); }
  .dot.active { width: 15px; height: 15px; background: var(--pink); }

  /* footer */
  .site-footer { left: 0; top: 970px; width: 798px; height: 112px; background: var(--band); }
  .footer-links { left: 100px; top: 1024px; font-size: 8.5px; color: var(--blue); }
  .footer-about { left: 503px; top: 985px; width: 200px; }
  .footer-title { font-size: 12.5px; color: var(--blue); margin-bottom: 4px; }
  .footer-text { font-family: "Roboto", sans-serif; font-size: 6px; line-height: 14px; color: var(--grey-text); }
  .copyright { left: 0; top: 1063px; width: 798px; text-align: center; font-family: "Roboto", sans-serif; font-size: 7.5px; color: var(--grey-text); }
</style>
</head>
<body>
<div class="page">

  <header class="site-header abs">
    <div class="brand abs">
      <span class="brand-mark"></span>
      <span class="brand-name">FixTrade</span>
    </div>
    <nav class="nav abs">
      <span>HOME</span>
      <span>DEVICE CATALOG</span>
    </nav>
    <svg class="account abs" width="16" height="18" viewBox="0 0 16 18" aria-label="Account">
      <circle cx="8" cy="5" r="4" fill="var(--blue)"/>
      <path d="M1 17 Q1 10 8 10 Q15 10 15 17 Z" fill="var(--blue)"/>
    </svg>
  </header>

  <section class="category category-phones abs" role="img" aria-label="Photo of a smartphone floating above an open hand by a lake">
    <h2 class="category-title">PHONES</h2>
    <p class="category-sub">All kinds of phones including smartphones</p>
    <span class="browse-btn">BROWSE</span>
  </section>
  <section class="category category-tablets abs" role="img" aria-label="Photo of a tablet with keyboard beside a potted plant on a desk">
    <h2 class="category-title">TABLETS</h2>
    <p class="category-sub">All kinds of tablets</p>
    <span class="browse-btn">BROWSE</span>
  </section>

  <article class="step abs" style="left:98px">
    <h3 class="step-title">QUOTE</h3>
    <p class="step-body">Get an exact quote for your exact device and its condition. No guess, no mess. Start by choosing a catagory above and find your device and condition to get a precise dollar amount.</p>
  </article>
  <article class="step abs" style="left:310px">
    <h3 class="step-title">BRING</h3>
    <p class="step-body">Bring your device into any one of <a>our convenient locations</a>. We'll pull up your quote right away.</p>
  </article>
  <article class="step abs" style="left:521px">
    <h3 class="step-title">GET PAID</h3>
    <p class="step-body">Get money as soon as we receive your device. We'll review the condition and let you know if there are any adjustments. Payment methods coming soon.</p>
  </article>

  <h2 class="reviews-title abs">REVIEWS</h2>

  <svg width="0" height="0" class="abs" aria-hidden="true"><defs><polygon id="s" fill="var(--star)" points="7.5,0.5 9.4,5.4 14.5,5.6 10.5,8.8 11.9,13.9 7.5,11 3.1,13.9 4.5,8.8 0.5,5.6 5.6,5.4"/></defs></svg>

  <article class="review abs" style="left:100px">
    <div class="reviewer"><span class="avatar" role="img" aria-label="Reviewer portrait"></span>Mara Velden</div>
    <h4 class="review-source">VERIFIED REVIEW</h4>
    <p class="review-text">Thank you for the good and reliable service. Highly recommend this place. They are professionals.</p>
    <svg class="stars" width="80" height="15" viewBox="0 0 80 15"><use href="#s"/><use href="#s" x="16"/><use href="#s" x="32"/><use href="#s" x="48"/><use href="#s" x="64"/></svg>
  </article>
  <article class="review abs" style="left:312px">
    <div class="reviewer"><span class="avatar" role="img" aria-label="Reviewer portrait"></span>Mara Velden</div>
    <h4 class="review-source">VERIFIED REVIEW</h4>
    <p class="review-text">Thank you for the good and reliable service. Highly recommend this place. They are professionals.</p>
    <svg class="stars" width="80" height="15" viewBox="0 0 80 15"><use href="#s"/><use href="#s" x="16"/><use href="#s" x="32"/><use href="#s" x="48"/><use href="#s" x="64"/></svg>
  </article>
  <article class="review abs" style="left:524px">
    <div class="reviewer"><span class="avatar" role="img" aria-label="Reviewer portrait"></span>Mara Velden</div>
    <h4 class="review-source">VERIFIED REVIEW</h4>
    <p class="review-text">Thank you for the good and reliable service. Highly recommend this place. They are professionals.</p>
    <svg class="stars" width="80" height="15" viewBox="0 0 80 15"><use href="#s"/><use href="#s" x="16"/><use href="#s" x="32"/><use href="#s" x="48"/><use href="#s" x="64"/></svg>
  </article>

  <div class="dots abs"><span class="dot"></span><span class="dot active"></span><span class="dot"></span></div>

  <footer class="site-footer abs"></footer>
  <p class="footer-links abs">FAQ | PRIVACY POLICY</p>
  <div class="footer-about abs">
    <h4 class="footer-title">FIXTRADE</h4>
    <p class="footer-text">We are a leading company in the industry of computer and phone repairs throughout Florida. Circuit &amp; Cell Co. is the place to go for an experienced, yet affordable cell phone and computer repair store!</p>
  </div>
  <p class="copyright abs">© FixTrade</p>

</div>
</body>
</html>
```